Vantrel Furniture Store needs an advertizing display

We just launched a furniture store in a place where not many people know us. So we need to display two vertical advertising banners (60cm x 160cm) to explain to the people our added value and our variety of products. We sell wooden furniture, chairs, upholstery, lamps and matresses. We diferenciate ourselves from the competition for our good quality and low prices. One banner needs to emphatize on our added value wich is "High end furniture at low prices". The other one needs to list our variety of products with prices starting at... Im uploading some images of the pieces we sell along with our logo.

Target Market(s)

People who want to improve their home decoration or who just moved to a new home

Industry/Entity Type

Furniture Store

Font styles to use
Sans Serif

Requirements
Must have
• One banner must have the look and feel of the brand (www.vantrel-example.com.mx) to comunicate our streghts which are high end products at affordable prices.
• The other one should have the variety of products we sell (wooden furniture, upholstery, matresses, lamps and chairs) with the lowest prices featured.

```html
<!DOCTYPE html>
<html lang="en">
<head>
<meta charset="utf-8">
<title>Vantrel Furniture Store – Banners</title>
<link href="https://fonts.googleapis.com/css2?family=Archivo:wght@400;700;800;900&display=swap" rel="stylesheet">
<style>
  :root{
    --stage:#000000;
    --paper:#ffffff;
    --lime:#b5e61d;
    --ink:#58585a;
    --forest:#1f6f1c;
    --forest-mid:#3c8c2a;
    --badge:#ffec00;
    --badge-text:#e4002b;
    --string:#555555;
  }
  html,body{margin:0;padding:0;width:1200px;height:1200px;overflow:hidden;background:var(--stage);}
  .stage{display:block;width:1200px;height:1200px;}
  .headline{font-family:"Archivo",Arial,sans-serif;font-weight:800;fill:var(--ink);}
  .headline-small{font-family:"Archivo",Arial,sans-serif;font-weight:800;fill:var(--paper);}
  .value-line{font-family:"Archivo",Arial,sans-serif;font-weight:800;fill:var(--paper);}
  .value-accent{font-family:"Archivo",Arial,sans-serif;font-weight:800;fill:var(--lime);}
  .categories{font-family:"Archivo",Arial,sans-serif;font-weight:800;fill:var(--ink);font-size:20px;}
  .brand-name{font-family:"Archivo",Arial,sans-serif;font-weight:700;fill:var(--paper);font-size:48px;}
  .address{font-family:"Archivo",Arial,sans-serif;font-weight:400;fill:var(--ink);font-size:20px;}
  .price-tag{font-family:"Archivo",Arial,sans-serif;font-weight:800;fill:var(--badge-text);font-size:13px;}
</style>
</head>
<body>
<svg class="stage" viewBox="0 0 1500 1500" xmlns="http://www.w3.org/2000/svg">
  <defs>
    <linearGradient id="collage-fill" x1="0" y1="0" x2="0" y2="1">
      <stop offset="0" stop-color="#9fd21f"/>
      <stop offset="0.3" stop-color="#6fae28"/>
      <stop offset="0.65" stop-color="#3c8c2a"/>
      <stop offset="1" stop-color="#1f6f1c"/>
    </linearGradient>
  </defs>

  <!-- Banner: added value -->
  <g class="banner banner-value">
    <rect class="banner-sheet" x="174" y="46" width="529" height="1409" fill="var(--paper)"/>
    <rect class="banner-panel" x="212" y="124" width="446" height="836" fill="var(--lime)"/>
    <line x1="284" y1="46" x2="284" y2="142" stroke="var(--string)" stroke-width="3"/>
    <line x1="606" y1="46" x2="606" y2="142" stroke="var(--string)" stroke-width="3"/>
    <circle cx="284" cy="155" r="13" fill="var(--paper)"/>
    <circle cx="606" cy="155" r="13" fill="var(--paper)"/>

    <text class="headline" x="255" y="328" font-size="112" textLength="358" lengthAdjust="spacingAndGlyphs">COME</text>
    <text class="headline" x="255" y="395" font-size="78" textLength="270" lengthAdjust="spacingAndGlyphs">CHECK</text>
    <text class="headline-small" x="540" y="366" font-size="36" textLength="77" lengthAdjust="spacingAndGlyphs">OUT</text>
    <text class="headline-small" x="538" y="397" font-size="36" textLength="80" lengthAdjust="spacingAndGlyphs">OUR</text>
    <text class="headline" x="255" y="458" font-size="76" textLength="362" lengthAdjust="spacingAndGlyphs">PRODUCT</text>

    <rect class="collage" role="img" aria-label="Illustration of assorted furniture silhouettes piled together in green tones" x="212" y="520" width="446" height="440" fill="url(#collage-fill)"/>

    <g class="value-message">
      <text class="value-line" x="435" y="800" text-anchor="middle" font-size="40" textLength="360" lengthAdjust="spacingAndGlyphs">HIGH END FURNITURE</text>
      <text class="value-accent" x="435" y="858" text-anchor="middle" font-size="52" textLength="360" lengthAdjust="spacingAndGlyphs">AT LOW PRICES</text>
      <rect x="375" y="884" width="120" height="5" fill="var(--lime)"/>
    </g>

    <text class="categories" x="212" y="998" textLength="446" lengthAdjust="spacingAndGlyphs">CHAIRS | UPHOLSTERY | LAMPS | MATRESSES</text>

    <rect class="brand-block" x="330" y="1097" width="216" height="213" fill="var(--lime)"/>
    <text class="brand-name" x="438" y="1222" text-anchor="middle">Vantrel</text>

    <text class="address" x="433" y="1366" text-anchor="middle">Calle Robles 48, Colonia Arboleda,</text>
    <text class="address" x="433" y="1391" text-anchor="middle">05020 Ciudad de México, D.F., Mexique</text>
  </g>

  <!-- Banner: product range -->
  <g class="banner banner-range">
    <rect class="banner-sheet" x="782" y="46" width="529" height="1409" fill="var(--paper)"/>
    <rect class="banner-panel" x="820" y="124" width="446" height="836" fill="var(--lime)"/>
    <line x1="891" y1="46" x2="891" y2="142" stroke="var(--string)" stroke-width="3"/>
    <line x1="1214" y1="46" x2="1214" y2="142" stroke="var(--string)" stroke-width="3"/>
    <circle cx="891" cy="155" r="13" fill="var(--paper)"/>
    <circle cx="1214" cy="155" r="13" fill="var(--paper)"/>

    <text class="headline" x="862" y="305" font-size="112" textLength="360" lengthAdjust="spacingAndGlyphs">COME</text>
    <text class="headline" x="862" y="372" font-size="78" textLength="270" lengthAdjust="spacingAndGlyphs">CHECK</text>
    <text class="headline-small" x="1147" y="344" font-size="36" textLength="77" lengthAdjust="spacingAndGlyphs">OUT</text>
    <text class="headline-small" x="1145" y="376" font-size="36" textLength="80" lengthAdjust="spacingAndGlyphs">OUR</text>
    <text class="headline" x="862" y="437" font-size="76" textLength="363" lengthAdjust="spacingAndGlyphs">PRODUCT</text>

    <g class="product-grid">
      <rect role="img" aria-label="Photo of a black stacking chair" x="828" y="521" width="211" height="211" fill="#e9e9e9"/>
      <rect role="img" aria-label="Photo of a dark wooden bed with white linen" x="1046" y="521" width="211" height="211" fill="#c9c3bb"/>
      <rect role="img" aria-label="Photo of a light wooden desk with a laptop" x="828" y="739" width="211" height="211" fill="#6e6860"/>
      <rect role="img" aria-label="Photo of a mustard chair with wooden legs" x="1046" y="739" width="211" height="211" fill="#e6e4dc"/>

      <circle cx="859" cy="698" r="28" fill="var(--badge)"/>
      <text class="price-tag" x="859" y="703" text-anchor="middle">PRICE</text>
      <circle cx="1080" cy="698" r="28" fill="var(--badge)"/>
      <text class="price-tag" x="1080" y="703" text-anchor="middle">PRICE</text>
      <circle cx="859" cy="918" r="28" fill="var(--badge)"/>
      <text class="price-tag" x="859" y="923" text-anchor="middle">PRICE</text>
      <circle cx="1080" cy="918" r="28" fill="var(--badge)"/>
      <text class="price-tag" x="1080" y="923" text-anchor="middle">PRICE</text>
    </g>

    <text class="categories" x="820" y="997" textLength="446" lengthAdjust="spacingAndGlyphs">CHAIRS | UPHOLSTERY | LAMPS | MATRESSES</text>

    <rect class="brand-block" x="938" y="1096" width="216" height="213" fill="var(--lime)"/>
    <text class="brand-name" x="1046" y="1221" text-anchor="middle">Vantrel</text>

    <text class="address" x="1041" y="1365" text-anchor="middle">Calle Robles 48, Colonia Arboleda,</text>
    <text class="address" x="1041" y="1390" text-anchor="middle">05020 Ciudad de México, D.F., Mexique</text>
  </g>
</svg>
</body>
</html>
```